Business card for psychiatrist

Business card design project for a psychiatristWe would like to have the impression of 1. We (patient and the doctor) are working together.2. Light the way so that patients can see where they are going and what their goals are.3. One side of the business card will have the letter "BFP" which stands for Brynmoor Family Psychiatry.4. The other side of the business card will have the address, phone number, name of the psychiatrist, website, etc.5. A logo could go into either side of the business card. Let's see what looks better.
Business card design project for a psychiatrist
We would like to have the impression of
1. We (patient and the doctor) are working together.
2. Light the way so that patients can see where they are going and what their goals are.
3. One side of the business card will have the letter "BFP" which stands for Brynmoor Family Psychiatry.
4. The other side of the business card will have the address, phone number, name of the psychiatrist, website, etc.
5. A logo could go into either side of the business card. Let's see what looks better.

```html
<!DOCTYPE html>
<html lang="en">
<head>
<meta charset="utf-8">
<title>Brynmoor Family Psychiatry – Business Card</title>
<link rel="stylesheet" href="https://fonts.googleapis.com/css2?family=Montserrat:wght@600;700&family=Roboto:wght@400;500&display=swap">
<style>
  :root {
    --bg: #1c1c1c;
    --card: #ffffff;
    --green: #7dbf3a;
    --blue: #2f9fdb;
    --grey: #a3a3a3;
    --orange: #f29a26;
  }
  * { box-sizing: border-box; margin: 0; padding: 0; }
  html, body { width: 1200px; height: 1200px; overflow: hidden; }
  body {
    background: var(--bg);
    font-family: "Roboto", sans-serif;
    position: relative;
  }
  .card {
    position: absolute;
    left: 150px;
    width: 900px;
    height: 514px;
    background: var(--card);
    border-radius: 28px;
  }
  .card-back { top: 50px; display: flex; align-items: center; justify-content: center; gap: 22px; }
  .card-front { top: 636px; }

  .mark-dot { width: 70px; height: 70px; border-radius: 50%; background: var(--orange); flex: none; }
  .mark-name {
    font-family: "Montserrat", sans-serif; font-weight: 700;
    font-size: 86px; color: var(--green); letter-spacing: 2px;
  }

  .front-brand { position: absolute; left: 48px; top: 44px; display: flex; align-items: center; gap: 20px; }
  .front-brand .mark-dot { width: 96px; height: 96px; }
  .front-brand .mark-name { font-size: 80px; }

  .practice-name {
    position: absolute; right: 50px; top: 118px; text-align: right;
    font-family: "Montserrat", sans-serif; font-weight: 700; color: var(--green);
  }
  .practice-name .line1 { font-size: 62px; line-height: 1; letter-spacing: 1px; }
  .practice-name .line2 { font-size: 27px; letter-spacing: 1.5px; margin-top: 4px; }

  .person { position: absolute; left: 48px; top: 270px; }
  .person-name {
    font-family: "Montserrat", sans-serif; font-weight: 700;
    font-size: 46px; color: var(--blue); line-height: 1; letter-spacing: 1px;
  }
  .person-title {
    font-family: "Montserrat", sans-serif; font-weight: 600;
    font-size: 21px; color: var(--green); letter-spacing: .5px; margin-top: 4px;
  }
  .rule-blue { position: absolute; left: 48px; top: 356px; width: 560px; height: 2px; background: var(--blue); }
  .rule-green { position: absolute; right: 50px; top: 356px; width: 250px; height: 2px; background: var(--green); }

  .contacts { position: absolute; left: 48px; top: 374px; list-style: none; }
  .contacts li { display: flex; align-items: center; gap: 14px; font-size: 22px; color: var(--blue); height: 36px; }
  .contacts svg { width: 26px; height: 26px; flex: none; }

  .address {
    position: absolute; right: 50px; top: 374px; text-align: right;
    font-size: 22px; line-height: 34px; color: var(--blue);
  }
</style>
</head>
<body>
  <section class="card card-back">
    <span class="mark-dot"></span>
    <span class="mark-name">BFP</span>
  </section>

  <section class="card card-front">
    <div class="front-brand">
      <span class="mark-dot"></span>
      <span class="mark-name">BFP</span>
    </div>

    <div class="practice-name">
      <div class="line1">BRYNMOOR</div>
      <div class="line2">FAMILY PSYCHIATRY</div>
    </div>

    <div class="person">
      <div class="person-name">DANIEL REYES</div>
      <div class="person-title">MANAGING DIRECTOR</div>
    </div>

    <div class="rule-blue"></div>
    <div class="rule-green"></div>

    <ul class="contacts">
      <li>
        <svg viewBox="0 0 26 26" aria-hidden="true"><circle cx="13" cy="13" r="13" fill="#7dbf3a"/><path d="M9 7.5c.6-.5 1.3-.4 1.7.2l1.2 1.9c.3.5.2 1.1-.2 1.5l-.8.7c.6 1.4 1.7 2.6 3.1 3.3l.8-.8c.4-.4 1-.5 1.5-.2l1.9 1.2c.6.4.7 1.1.2 1.7-1 1.2-2.4 1.4-3.8.7-2.6-1.3-4.6-3.4-5.8-6-.6-1.4-.3-2.8.2-4.2z" fill="#fff"/></svg>
        844-555-0142
      </li>
      <li>
        <svg viewBox="0 0 26 26" aria-hidden="true"><circle cx="13" cy="13" r="13" fill="#7dbf3a"/><rect x="7" y="8.5" width="12" height="9" rx="1" fill="none" stroke="#fff" stroke-width="1.5"/><path d="M7.5 9.2l5.5 4.5 5.5-4.5" fill="none" stroke="#fff" stroke-width="1.5"/></svg>
        daniel@brynmoorfamilypsychiatry.com
      </li>
      <li>
        <svg viewBox="0 0 26 26" aria-hidden="true"><circle cx="13" cy="13" r="13" fill="#7dbf3a"/><g fill="none" stroke="#fff" stroke-width="1.3"><circle cx="13" cy="13" r="6.5"/><ellipse cx="13" cy="13" rx="2.8" ry="6.5"/><path d="M6.5 13h13M7.5 9.8h11M7.5 16.2h11"/></g></svg>
        www.brynmoorfamilypsychiatry.com
      </li>
    </ul>

    <address class="address" style="font-style:normal">
      418 Harbor Street NE<br>
      Suite 210, Lakeview<br>
      MI 49001
    </address>
  </section>
</body>
</html>
```